Business Card Design EFTPOS Comparison site

At QuoteHarbor.com.au we are a free service that allows our customers to get up to five quotes from our panel of suppliers for a range of BUSINESS related products and services. These products include eftpos / credit card machines, bank accounts, insurance, signage,office furniture etc. basically anything that a small business would need.
The process is done in 3 steps; 1) register your enquiry 2) we source and provide the five cheapest quotes 3) then select the supplier of your choice,the process is simple ABC and is FREE.
Please visit the soon to be revamped website to see our logo.
Target Market(s)
Small business operators
Industry/Entity Type
Small Business
Requirements
Must have
- Double Sided card

```html
<!DOCTYPE html>
<html lang="en">
<head>
<meta charset="utf-8">
<title>QuoteHarbor Business Card</title>
<link rel="stylesheet" href="https://fonts.googleapis.com/css2?family=Open+Sans:wght@400;700&family=Kalam:wght@700&display=swap">
<style>
  :root {
    --stage: #2a2a2a;
    --card: #ffffff;
    --pink: #e5186f;
    --blue: #3cc4ea;
    --green: #9ed94a;
    --grey-1: #cdcdcd;
    --grey-2: #dadada;
    --grey-3: #e7e7e7;
    --brand: #f07f1a;
    --ink: #222222;
    --on-band: #ffffff;
  }
  * { margin: 0; padding: 0; box-sizing: border-box; }
  html, body { width: 1200px; height: 1001px; overflow: hidden; }
  body {
    background: var(--stage);
    display: flex;
    align-items: center;
    justify-content: center;
    gap: 40px;
    font-family: "Open Sans", Arial, sans-serif;
  }
  .card {
    width: 540px;
    height: 318px;
    background: var(--card);
    box-shadow: 0 6px 18px rgba(0,0,0,.35);
  }
  .card svg { display: block; width: 100%; height: 100%; }
  .band-pink { fill: var(--pink); }
  .band-blue { fill: var(--blue); }
  .band-green { fill: var(--green); }
  .tone-1 { fill: var(--grey-1); }
  .tone-2 { fill: var(--grey-2); }
  .tone-3 { fill: var(--grey-3); }
  .brand-dot { fill: var(--brand); }
  .brand-name { fill: var(--brand); font-family: "Open Sans", Arial, sans-serif; font-weight: 700; font-size: 26px; }
  .person-name { fill: var(--ink); font-family: "Kalam", cursive; font-weight: 700; font-size: 22px; }
  .person-role { fill: var(--ink); font-family: "Open Sans", Arial, sans-serif; font-size: 10px; }
  .name-rule { stroke: var(--pink); stroke-width: 2; }
  .band-text { fill: var(--on-band); font-family: "Open Sans", Arial, sans-serif; font-size: 10.5px; }
  .web-text { fill: var(--ink); font-family: "Open Sans", Arial, sans-serif; font-size: 10.5px; }
</style>
</head>
<body>

  <section class="card card-front" aria-label="Card front">
    <svg viewBox="0 0 540 318" xmlns="http://www.w3.org/2000/svg">
      <g class="contact-name">
        <text class="person-name" x="378" y="44">Mara Ellison</text>
        <line class="name-rule" x1="372" y1="50" x2="540" y2="50"/>
        <circle class="band-pink" cx="372" cy="50" r="2.5"/>
        <text class="person-role" x="378" y="63">creative director</text>
      </g>

      <g class="brand">
        <circle class="brand-dot" cx="52" cy="106" r="9"/>
        <text class="brand-name" x="68" y="115">QuoteHarbor</text>
      </g>

      <g class="stripes">
        <polygon class="band-pink" points="0,168 443,168 410.7,188 0,188"/>
        <polygon class="band-blue" points="0,188 410.7,188 378.3,208 0,208"/>
        <polygon class="band-green" points="0,208 378.3,208 346,228 0,228"/>
        <polygon class="tone-1" points="443,168 540,168 540,188 410.7,188"/>
        <polygon class="tone-2" points="410.7,188 540,188 540,208 378.3,208"/>
        <polygon class="tone-3" points="378.3,208 540,208 540,228 346,228"/>
      </g>

      <g class="contact-details">
        <text class="band-text" x="36" y="182">a: 48 Harbour Lane, Wrenmoor NSW 2150</text>
        <text class="band-text" x="36" y="202">t: 02 9555 0142  /  f: 02 9555 0143</text>
        <text class="band-text" x="36" y="222">e: hello@quoteharbor.com.au</text>
        <text class="web-text" x="36" y="256">w: quoteharbor.com.au</text>
      </g>
    </svg>
  </section>

  <section class="card card-back" aria-label="Card back">
    <svg viewBox="0 0 540 318" xmlns="http://www.w3.org/2000/svg">
      <g class="brand">
        <circle class="brand-dot" cx="197" cy="96" r="9"/>
        <text class="brand-name" x="213" y="105">QuoteHarbor</text>
      </g>

      <g class="stripes">
        <polygon class="tone-1" points="0,168 140,168 161.7,188 0,188"/>
        <polygon class="tone-2" points="0,188 161.7,188 183.3,208 0,208"/>
        <polygon class="tone-3" points="0,208 183.3,208 205,228 0,228"/>
        <polygon class="band-pink" points="140,168 540,168 540,188 161.7,188"/>
        <polygon class="band-blue" points="161.7,188 540,188 540,208 183.3,208"/>
        <polygon class="band-green" points="183.3,208 540,208 540,228 205,228"/>
      </g>

      <text class="band-text tagline" x="178" y="182">advanced business solution</text>
    </svg>
  </section>

</body>
</html>
```